Shine Bay Auto Care Business Card

2 side business card design for an auto detailing business

Target Market(s)

Auto detailing

Contact Information for Business Card

Things included

The business name “Shine Bay Auto Care”
Marc Tessier
(403)261-9047
Pinewood Falls, Sk

Services offered - complete interior& exterior detail
- paint correction & protection
- ceramic coating
- trim restore
- auto carpet & seat cleaning

Requirements
Must have
• Colours that are in my logo

Services offered

My name Marc Tessier
403-261-9047
Pinewood Falls, Sk

Not too sure in what order for these ?
Website. Shinebayautocare.com
Instagram Shinebayautocare
Email. Shinebayautoac@mailbox-example.com

```html
<!DOCTYPE html>
<html lang="en">
<head>
<meta charset="utf-8">
<title>Shine Bay Auto Care – Business Card</title>
<link rel="stylesheet" href="https://fonts.googleapis.com/css2?family=Arimo:wght@400;700&family=Montserrat:wght@600&display=swap">
<style>
  :root {
    --bg: #a4a4a4;
    --red: #8c0000;
    --black: #000000;
    --white: #ffffff;
    --rule: rgba(255,255,255,0.7);
  }
  * { margin: 0; padding: 0; box-sizing: border-box; }
  html, body { width: 1200px; height: 1200px; overflow: hidden; }
  body { background: var(--bg); position: relative; font-family: "Arimo", Arial, sans-serif; }

  .card { position: absolute; top: 303px; height: 594px; border-radius: 14px; overflow: hidden; }
  .card--front { left: 200px; width: 370px; }
  .card--back { left: 600px; width: 361px; }
  .card__bg { position: absolute; inset: 0; width: 100%; height: 100%; }

  .line { position: absolute; left: 0; width: 100%; text-align: center; color: var(--white); white-space: nowrap; }

  .brand-ring { position: absolute; left: 50%; top: 82px; width: 96px; height: 96px; margin-left: -48px; border-radius: 50%; border: 5px solid var(--white); }
  .card--back .brand-ring { border-color: var(--red); }
  .brand-name { position: absolute; left: 0; width: 100%; text-align: center; font-weight: 700; color: var(--white); white-space: nowrap; }
  .card--back .brand-name { color: var(--black); }
  .brand-name__main { top: 192px; font-size: 38px; letter-spacing: 0.01em; }
  .brand-name__sub { top: 239px; font-size: 19px; letter-spacing: 0.75em; padding-left: 0.75em; word-spacing: -0.3em; }

  .services-title { top: 338px; font-size: 18px; font-weight: 700; }
  .services-sub { top: 362px; font-size: 13.5px; }
  .service { font-size: 19.5px; }
  .service--1 { top: 389px; } .service--2 { top: 416px; } .service--3 { top: 443px; } .service--4 { top: 470px; }
  .rule { position: absolute; height: 1px; background: var(--rule); }
  .handle { top: 542px; font-size: 16.5px; }
  .social-dot { position: absolute; left: 174px; top: 515px; width: 22px; height: 22px; border-radius: 50%; background: var(--white); }

  .person { top: 352px; font-family: "Montserrat", Arial, sans-serif; font-weight: 600; font-size: 22px; letter-spacing: 0.04em; }
  .contact { font-size: 17px; }
  .contact--phone { top: 426px; } .contact--mail { top: 448px; } .contact--web { top: 469px; }
  .location { top: 529px; font-size: 17px; }
  .icon { position: absolute; }
</style>
</head>
<body>

<section class="card card--front">
  <svg class="card__bg" viewBox="0 0 370 594" aria-hidden="true">
    <rect width="370" height="594" fill="var(--black)"/>
    <path d="M0 284 Q185 352 370 284 L370 594 L0 594 Z" fill="var(--red)"/>
  </svg>
  <div class="brand-ring"></div>
  <div class="brand-name brand-name__main">SHINE BAY</div>
  <div class="brand-name brand-name__sub">AUTO CARE</div>

  <div class="rule" style="left:34px; top:352px; width:49px;"></div>
  <div class="rule" style="left:287px; top:352px; width:49px;"></div>
  <div class="line services-title">SERVICES OFFERED</div>
  <div class="line services-sub">COMPLETE INTERIOR &amp; EXTERIOR DETAIL</div>
  <div class="line service service--1">Paint correction &amp; protection</div>
  <div class="line service service--2">Ceramic coating</div>
  <div class="line service service--3">Trim restore</div>
  <div class="line service service--4">Auto carpet &amp; seat cleaning</div>

  <div class="rule" style="left:33px; top:526px; width:137px;"></div>
  <div class="rule" style="left:200px; top:526px; width:131px;"></div>
  <div class="social-dot"></div>
  <div class="line handle">Shinebayautocare</div>
</section>

<section class="card card--back">
  <svg class="card__bg" viewBox="0 0 361 594" aria-hidden="true">
    <rect width="361" height="594" fill="var(--white)"/>
    <path d="M0 284 Q180.5 352 361 284 L361 594 L0 594 Z" fill="var(--red)"/>
  </svg>
  <div class="brand-ring"></div>
  <div class="brand-name brand-name__main">SHINE BAY</div>
  <div class="brand-name brand-name__sub">AUTO CARE</div>

  <div class="line person">MARC TESSIER</div>

  <div class="rule" style="left:86px; top:405px; width:51px;"></div>
  <div class="rule" style="left:230px; top:405px; width:46px;"></div>
  <svg class="icon" style="left:140px; top:392px;" width="88" height="26" viewBox="0 0 88 26" aria-hidden="true">
    <g fill="none" stroke="var(--white)" stroke-width="1.4">
      <circle cx="13" cy="13" r="11.5"/>
      <circle cx="43" cy="13" r="11.5"/>
      <circle cx="72" cy="13" r="11.5"/>
    </g>
    <path d="M9 7.5 l2.5 -0.5 l1.5 3.5 l-1.6 1.2 q1 2.6 3.4 3.8 l1.3 -1.5 l3.4 1.6 l-0.6 2.5 q-6 0.5 -9.9 -10.6 z" fill="var(--white)"/>
    <rect x="36.5" y="8.5" width="13" height="9" fill="var(--white)"/>
    <path d="M36.5 8.5 L43 13.5 L49.5 8.5" fill="none" stroke="var(--red)" stroke-width="1.1"/>
    <circle cx="72" cy="13" r="6.5" fill="none" stroke="var(--white)" stroke-width="1.4"/>
    <path d="M65.5 13 h13 M72 6.5 q-3.5 6.5 0 13 M72 6.5 q3.5 6.5 0 13" fill="none" stroke="var(--white)" stroke-width="1.1"/>
  </svg>
  <div class="line contact contact--phone">(403)261-9047</div>
  <div class="line contact contact--mail">Shinebayautocare@mailbox-example.com</div>
  <div class="line contact contact--web">www.Shinebayautocare.com</div>

  <div class="rule" style="left:87px; top:514px; width:76px;"></div>
  <div class="rule" style="left:198px; top:514px; width:83px;"></div>
  <svg class="icon" style="left:168px; top:501px;" width="26" height="26" viewBox="0 0 26 26" aria-hidden="true">
    <circle cx="13" cy="13" r="11.5" fill="none" stroke="var(--white)" stroke-width="1.4"/>
    <path d="M13 20 q-5 -5.5 -5 -8.5 a5 5 0 0 1 10 0 q0 3 -5 8.5 z" fill="var(--white)"/>
    <circle cx="13" cy="11.5" r="1.9" fill="var(--red)"/>
  </svg>
  <div class="line location">Pinewood Falls, Sk</div>
</section>

</body>
</html>
```